Computer Training in the Education sector - Letterhead

We need a new letter head to be designed for the company. We provide computer training fro the Education Sector, both primary and private tertiary providers. The colours will need to tie in with the website www.lanternpathlearning.co.nz.
The company name is Lantern Path Co with the tag line of Computer Training for Educators.
The footer will need to have the following detail...
0508 KEY MENTOR
027 813 459
www.lanternpathlearning.co.nz / lessons@lanternpathlearning.co.nz
Updates

Thanks for the designs so far.

Some have watermarks in the background. Please don't worry about using watermarks as I will not be using a watermark in in a final design.
Regards,
Morris

Thank you for all the designs and the effort. There was some great concepts that came through.

Cheers
Morris

Industry/Entity Type

Computer

```html
<!DOCTYPE html>
<html lang="en">
<head>
<meta charset="utf-8">
<title>Lantern Path Co – Letterhead</title>
<link rel="stylesheet" href="https://fonts.googleapis.com/css2?family=Open+Sans:wght@400;600;700&display=swap">
<style>
  :root {
    --backdrop: #e4e5e7;
    --paper: #ffffff;
    --brand-blue: #1f6fb8;
    --brand-orange: #f0952e;
    --brand-green: #6bbf3a;
    --wash-tint: #d6e8f4;
    --ink: #1b1b1b;
  }
  * { box-sizing: border-box; margin: 0; padding: 0; }
  html, body {
    width: 1200px; height: 900px; overflow: hidden;
    background: var(--backdrop);
    font-family: "Open Sans", Arial, sans-serif;
  }
  .letterhead {
    position: absolute;
    left: 300px; top: 24px;
    width: 600px; height: 852px;
    background: var(--paper);
    box-shadow: 0 2px 8px rgba(0,0,0,0.15);
    overflow: hidden;
  }
  .top-rule {
    position: absolute; left: 0; top: 5px;
    width: 600px; height: 3px;
    background: var(--brand-blue);
  }
  .top-rule-thin {
    position: absolute; left: 0; top: 11px;
    width: 600px; height: 1px;
    background: var(--brand-blue);
  }
  .header-rule {
    position: absolute; left: 90px; top: 66px;
    width: 510px; height: 1px;
    background: var(--brand-blue);
  }
  .brand-mark {
    position: absolute; left: 20px; top: 34px;
    display: flex; align-items: center; gap: 6px;
    font-size: 11px; font-weight: 600; color: var(--brand-blue);
  }
  .brand-mark .dot {
    width: 14px; height: 14px; border-radius: 50%;
    background: var(--brand-orange);
  }
  .masthead {
    position: absolute; right: 12px; top: 20px; text-align: right;
  }
  .company-name {
    font-size: 20px; font-weight: 400;
    color: var(--brand-blue); line-height: 1.15;
  }
  .tagline {
    font-size: 11px; font-weight: 600;
    color: var(--brand-green); line-height: 1.3; margin-top: 2px;
  }
  .footer-wash {
    position: absolute; left: 0; bottom: 0;
    width: 600px; height: 150px;
    background: linear-gradient(to bottom, rgba(214,232,244,0) 0%, var(--wash-tint) 100%);
  }
  .contact {
    position: absolute; left: 20px; bottom: 20px;
    font-size: 9.5px; font-weight: 600; color: var(--ink); line-height: 1.4;
  }
</style>
</head>
<body>
  <main class="letterhead">
    <div class="top-rule"></div>
    <div class="top-rule-thin"></div>
    <div class="header-rule"></div>

    <div class="brand-mark"><span class="dot"></span>Lantern Path Co</div>

    <header class="masthead">
      <h1 class="company-name">LANTERN PATH CO</h1>
      <p class="tagline">Computer Training for Educators.</p>
    </header>

    <div class="footer-wash" role="img" aria-label="Soft colour wash along the foot of the page"></div>

    <footer class="contact">
      <p>0508 KEY MENTOR</p>
      <p>027 813 459</p>
      <p>www.lanternpathlearning.co.nz / lessons@lanternpathlearning.co.nz</p>
    </footer>
  </main>
</body>
</html>
```